Logo & Visitenkarte für Gebäudereinigung
Der Designer konnte genau meine Ansprüche die ich gestellt habe erfüllen. Und war kreativ genau das was ich nicht so bin und ich genau deswegen ja auch einen Designer engagiert habe. Weiter zu enpfehlen!
Zielgruppe
Dienstleistung:
Als Gebäudereinigung bieten wir Reinigungsleistungen, wie Unterhaltsreinigung, Grundreinigung und Glasreinigung, Büroreinigung primär an Gewerbekunden an.
Zielkunden:
Zu unseren Kunden zählen Büroflächen.
Wobei unser Fokus vor allem auf Büros liegt und sich dahinter diverse Kunden verbergen, wie Kanzleien, IT-Firmen, Beratungsunternehmen, Finanzdienstleister, Produktionen etc., die Wert auf ein sauberes und professionelles Erscheinungsbild ihrer Gebäude legen. Die zielgruppe ist eher 'Nobel' gehobenes Milieu.
Aufgabenstellung
Werte & Image:
Qualität, Zuverlässigkeit, Kundenorientierung, Professionalität, exzellenter Service
Das Logo soll ein modernes und professionelles Image vermitteln, das unsere Dienstleistungen und unseren hohen Anspruch widerspiegelt.

```html
<!DOCTYPE html>
<html lang="de">
<head>
<meta charset="utf-8">
<title>VELMARO – Visitenkarte</title>
<link rel="stylesheet" href="https://fonts.googleapis.com/css2?family=Montserrat:wght@400;500;700&display=swap">
<style>
  :root {
    --navy: #323f6b;
    --navy-deep: #2b375e;
    --silver: #a3a5a8;
    --silver-light: #c4c6c9;
    --paper: #ffffff;
    --ink: #1f1f24;
    --backdrop: #e9eaec;
  }
  * { box-sizing: border-box; margin: 0; padding: 0; }
  html, body { width: 1200px; height: 1200px; overflow: hidden; }
  body {
    background: var(--backdrop);
    font-family: "Montserrat", sans-serif;
    display: flex; flex-direction: column; align-items: center; justify-content: center;
    gap: 50px;
  }
  .card {
    position: relative;
    width: 820px; height: 530px;
    overflow: hidden;
    box-shadow: 0 10px 30px rgba(30, 35, 60, .18);
  }
  .card--front { background: var(--navy); }
  .card--back { background: var(--paper); }

  .brand { position: absolute; display: flex; align-items: center; }
  .brand__dot {
    width: 62px; height: 62px; border-radius: 50%;
    border: 5px solid var(--silver);
  }
  .brand__divider { width: 1.5px; height: 96px; margin: 0 30px; }
  .brand__name {
    font-weight: 500; font-size: 50px; letter-spacing: 6px;
  }
  .card--front .brand { left: 50%; top: 50%; transform: translate(-50%, -50%); }
  .card--front .brand__divider { background: var(--silver); }
  .card--front .brand__name { color: var(--paper); }

  .card--back .brand { left: 58px; top: 60px; }
  .card--back .brand__dot { width: 50px; height: 50px; border-width: 4px; }
  .card--back .brand__divider { background: var(--silver-light); height: 80px; margin: 0 24px; }
  .card--back .brand__name { color: var(--navy); font-size: 40px; letter-spacing: 5px; }

  .person { position: absolute; left: 86px; top: 262px; color: var(--ink); }
  .person__name { font-weight: 700; font-size: 27px; }
  .person__role { font-size: 16px; margin-top: 6px; }
  .person__rule { width: 60px; height: 1.5px; background: var(--silver); margin: 18px 0 20px; }
  .person__address { font-size: 16px; line-height: 1.6; }

  .contact { position: absolute; right: 60px; top: 150px; list-style: none; color: var(--ink); }
  .contact li { display: flex; align-items: center; gap: 16px; font-size: 16px; height: 31px; }
  .contact svg { width: 20px; height: 20px; flex: none; }

  .band { position: absolute; left: 0; bottom: 0; width: 820px; height: 150px; }
</style>
</head>
<body>
  <section class="card card--front">
    <div class="brand">
      <span class="brand__dot"></span>
      <span class="brand__divider"></span>
      <span class="brand__name">VELMARO</span>
    </div>
  </section>

  <section class="card card--back">
    <div class="brand">
      <span class="brand__dot"></span>
      <span class="brand__divider"></span>
      <span class="brand__name">VELMARO</span>
    </div>

    <div class="person">
      <p class="person__name">Henrik Aldmann</p>
      <p class="person__role">Geschäftsführer</p>
      <div class="person__rule"></div>
      <p class="person__address">Lindenallee 27<br>40213 Feldhausen</p>
    </div>

    <ul class="contact">
      <li>
        <svg viewBox="0 0 24 24" fill="none" stroke="#9a9ca0" stroke-width="1.6"><path d="M5 3h4l2 5-2.5 1.5a11 11 0 0 0 6 6L16 13l5 2v4a2 2 0 0 1-2 2A17 17 0 0 1 3 5a2 2 0 0 1 2-2z"/></svg>
        +49 (0)4711 3 28 64-0
      </li>
      <li>
        <svg viewBox="0 0 24 24" fill="none" stroke="#9a9ca0" stroke-width="1.6"><rect x="6" y="3" width="12" height="6"/><rect x="3" y="9" width="18" height="8" rx="1"/><rect x="6" y="14" width="12" height="7"/></svg>
        +49 (0)4711 3 28 64-50
      </li>
      <li>
        <svg viewBox="0 0 24 24" fill="none" stroke="#9a9ca0" stroke-width="1.6"><rect x="7" y="2" width="10" height="20" rx="2"/><path d="M11 18h2"/></svg>
        +49 (0)172 9 83 15 40
      </li>
      <li>
        <svg viewBox="0 0 24 24" fill="none" stroke="#9a9ca0" stroke-width="1.6"><rect x="3" y="6" width="18" height="12"/><path d="M3 6l9 7 9-7"/></svg>
        kontakt@velmaro-service.de
      </li>
      <li>
        <svg viewBox="0 0 24 24" fill="none" stroke="#9a9ca0" stroke-width="1.6"><circle cx="12" cy="12" r="9"/><path d="M3 12h18M12 3c3 3 3 15 0 18M12 3c-3 3-3 15 0 18"/></svg>
        velmaro-service.de
      </li>
    </ul>

    <svg class="band" viewBox="0 0 820 150" preserveAspectRatio="none" aria-hidden="true">
      <polygon points="640,30 820,30 820,60 600,60" fill="var(--silver-light)"/>
      <polygon points="0,128 600,60 820,60 820,150 0,150" fill="var(--navy)"/>
    </svg>
  </section>
</body>
</html>
```